Label design for life altering nutraceutical bottle (60 pills)

We plan to market a form of Vitamin B3 known as nicotinamide riboside (NR) which is found in trace amounts in milk. At higher concentrations this compound can restore aged mitochondria (the energy cells in our bodies) to their youthful levels of activity. NR has the potential to extend years of healthy living and prevent many diseases associated with aging.

We will be selling NR is pill form (375 mg each) with 60 pills per bottle. Our company name is Silverpine Biologics. We need a design for the label to be placed on each pill bottle. The label itself is 19cm x 6cm

Target Market(s)

Health conscious consumers, Longevity, Nerve Pain, High Blood Pressure, Weight Loss

Industry/Entity Type

Nutrition

Logo Text

Silverpine Biologics

Font styles to use
Sans Serif

Colors
ffc214
ffffff

Requirements
Must have
• Language necessary on wraparound bottle label.
• 60 capsules, 375 mg, vegetarian capsule, gluten free, dietary supplement
• WARNING: Do not use if pregnant or nursing. If you are diabetic, have liver disease or stomach ulcers consult your health care practitioner before using this product.
• CAUTION: It is recommended to discontinue use 2 weeks before any elective surgery.
• Keep out of reach of children.
• These statements have not been evaluated by the National Remedy Standards Bureau. This product is not intended to diagnose, treat, cure or prevent any disease.
• US Supplement Facts Label
• "Supplement Facts"
• Serving Size 2 Capsules
• Servings Per Container 30
• Amount Per Serving
• Nicotinamide Riboside 1000mg
• % Daily Value
• 5000%
• Other Ingredients: Vegetable cellulose (capsule)
• Distributed By: Silverpine Biologics LLC, Las Vegas NV, (555) 555-0187, www.SilverpineBiologics.example, Info@SilverpineBiologics.example
Nice to have
• NR (in box in large letters, underneath, the words "Nicotinamide Riboside"
• under box, the words "Turn back the hands of time"
• "New!" in a prominent place on the label.

```html
<!DOCTYPE html>
<html lang="en">
<head>
<meta charset="utf-8">
<title>Nicotinamide Riboside NR – Silverpine Biologics label</title>
<link rel="stylesheet" href="https://fonts.googleapis.com/css2?family=Barlow:wght@200;400;500;600;700&family=Sacramento&display=swap">
<style>
  :root {
    --gold: #ffc214;
    --gold-deep: #f2a400;
    --amber: #e08a00;
    --pale: #fff6c8;
    --white: #ffffff;
    --ink: #1f1f1f;
    --nr-ink: #b87800;
  }
  * { margin: 0; padding: 0; box-sizing: border-box; }
  html, body { width: 1200px; height: 379px; overflow: hidden; background: var(--white); }
  body { font-family: "Barlow", Arial, sans-serif; color: var(--ink); }

  .label {
    position: relative;
    width: 1200px; height: 379px; overflow: hidden;
    background: linear-gradient(90deg, var(--white) 0%, var(--pale) 22%, var(--gold) 55%, var(--gold-deep) 100%);
  }
  .swoosh { position: absolute; inset: 0; }

  /* Left panel */
  .warnings { position: absolute; left: 30px; top: 32px; width: 270px; font-size: 13px; line-height: 1.35; }
  .notice { display: flex; margin-bottom: 16px; }
  .notice b { font-weight: 700; letter-spacing: .03em; width: 74px; flex: none; }
  .notice.caution b { width: 72px; }
  .bullets { list-style: none; }
  .bullets li { position: relative; padding-left: 16px; margin-bottom: 14px; }
  .bullets li::before { content: ""; position: absolute; left: 2px; top: 7px; width: 5px; height: 5px; border-radius: 50%; background: var(--ink); }

  /* Center */
  .photo-ring { position: absolute; left: 286px; top: -56px; width: 388px; height: 388px; border-radius: 50%; background: var(--gold-deep); opacity: .55; }
  .photo {
    position: absolute; left: 300px; top: -44px; width: 360px; height: 360px; border-radius: 50%;
    background: linear-gradient(180deg, #9cc3e6 0%, #c9def0 40%, #7c9a56 70%, #4f6b30 100%);
  }
  .title-glow { position: absolute; left: 604px; top: -52px; width: 264px; height: 264px; border-radius: 50%; background: radial-gradient(circle, var(--white) 0%, #fffbe3 60%, rgba(255,255,255,.6) 100%); }
  .new-badge {
    position: absolute; left: 296px; top: 6px; width: 76px; height: 76px; border-radius: 50%;
    background: var(--gold); border: 6px solid #ffd95a;
    display: flex; align-items: center; justify-content: center;
    font-weight: 700; font-size: 24px; color: var(--ink);
  }
  .product-name { position: absolute; left: 632px; top: 28px; width: 210px; text-align: center; font-weight: 700; font-size: 35px; line-height: 1.05; color: var(--ink); }
  .product-code { position: absolute; left: 686px; top: 100px; font-weight: 200; font-size: 84px; line-height: 1; color: var(--nr-ink); letter-spacing: 2px; }

  .badges { position: absolute; left: 646px; top: 220px; display: flex; gap: 12px; }
  .badge { width: 66px; text-align: center; font-size: 9.5px; line-height: 1.15; text-transform: uppercase; letter-spacing: .02em; }
  .badge svg { display: block; margin: 0 auto 5px; }
  .badge.wide { width: 80px; }

  .tagline { position: absolute; left: 350px; top: 318px; font-family: "Sacramento", cursive; font-size: 32px; color: var(--ink); }
  .count { position: absolute; left: 656px; top: 322px; font-size: 20px; display: flex; align-items: baseline; gap: 8px; }
  .count strong { font-weight: 700; font-size: 26px; }
  .count .divider { width: 2px; height: 24px; background: var(--gold); align-self: center; }

  /* Right panel */
  .facts { position: absolute; left: 902px; top: 32px; width: 266px; height: 200px; border: 3px solid var(--ink); padding: 8px 9px; background: rgba(255,226,120,.35); }
  .facts h2 { font-size: 25px; font-weight: 700; line-height: 1; margin-bottom: 8px; }
  .facts p { font-size: 12px; line-height: 1.45; }
  .facts .rule-thick { height: 5px; background: var(--ink); margin: 6px 0 6px; }
  .facts .rule { height: 3px; background: var(--ink); margin: 5px 0; }
  .facts .row { display: flex; justify-content: space-between; font-size: 12px; line-height: 1.4; }
  .facts .head { font-weight: 700; text-decoration: underline; }
  .facts .nutrient { text-decoration: underline; }
  .facts .nutrient span:nth-child(2) { margin-left: auto; margin-right: 14px; }

  .ingredients { position: absolute; left: 900px; top: 248px; font-size: 12px; }
  .ingredients b, .distributor b { font-weight: 700; }
  .distributor { position: absolute; left: 900px; top: 272px; font-size: 12px; display: flex; gap: 4px; line-height: 1.33; }
</style>
</head>
<body>
<div class="label">
  <svg class="swoosh" width="1200" height="379" viewBox="0 0 1200 379" aria-hidden="true">
    <path d="M0 250 C 250 210, 500 330, 760 300 S 1050 230, 1200 250 L1200 300 C 1000 290, 900 360, 650 370 S 200 300, 0 300 Z" fill="#ffffff" opacity=".55"/>
    <path d="M0 280 C 300 250, 480 350, 780 330 S 1050 270, 1200 290 L1200 379 L0 379 Z" fill="#ffd44d" opacity=".35"/>
  </svg>

  <section class="warnings">
    <p class="notice"><b>WARNING:</b><span>Do not use if pregnant or nursing. If you are diabetic, have liver disease or stomach ulcers consult your health care practitioner before using this product.</span></p>
    <p class="notice caution"><b>CAUTION:</b><span>It is recommended to discontinue use 2 weeks before any elective surgery.</span></p>
    <ul class="bullets">
      <li>Keep out of reach of children.</li>
      <li>These statements have not been evaluated by the National Remedy Standards Bureau. This product is not intended to diagnose, treat, cure or prevent any disease.</li>
    </ul>
  </section>

  <div class="photo-ring"></div>
  <div class="photo" role="img" aria-label="Photo of a smiling couple jogging outdoors under a blue sky"></div>
  <div class="title-glow"></div>
  <div class="new-badge">NEW</div>

  <h1 class="product-name">Nicotinamide Riboside</h1>
  <div class="product-code">NR</div>

  <div class="badges">
    <div class="badge">
      <svg width="54" height="54" viewBox="0 0 54 54" aria-hidden="true"><circle cx="27" cy="27" r="26" fill="#ffd84a"/><circle cx="27" cy="27" r="20" fill="#ffc214"/><path d="M17 36 C 17 22, 27 16, 38 16 C 38 28, 30 36, 17 36 Z" fill="#1f1f1f"/><path d="M15 40 L 30 25" stroke="#ffc214" stroke-width="2"/></svg>
      Vegetarian<br>Capsule
    </div>
    <div class="badge">
      <svg width="54" height="54" viewBox="0 0 54 54" aria-hidden="true"><circle cx="27" cy="27" r="26" fill="#ffd84a"/><circle cx="27" cy="27" r="20" fill="#ffc214"/><circle cx="27" cy="27" r="12" fill="none" stroke="#1f1f1f" stroke-width="3"/><path d="M27 18 V36 M22 23 L27 27 L32 23 M22 29 L27 33 L32 29" stroke="#1f1f1f" stroke-width="2" fill="none"/><path d="M18 18 L36 36" stroke="#1f1f1f" stroke-width="3"/></svg>
      Gluten<br>Free
    </div>
    <div class="badge wide">
      <svg width="54" height="54" viewBox="0 0 54 54" aria-hidden="true"><circle cx="27" cy="27" r="26" fill="#ffd84a"/><circle cx="27" cy="27" r="20" fill="#ffc214"/><path d="M17 24 C 18 16, 26 14, 30 16 C 29 22, 24 26, 17 24 Z" fill="#1f1f1f"/><rect x="22" y="27" width="18" height="8" rx="4" transform="rotate(-30 31 31)" fill="#1f1f1f"/><circle cx="22" cy="36" r="4" fill="#1f1f1f"/></svg>
      Dietary<br>Supplement
    </div>
  </div>

  <p class="tagline">Turn back the hands of time</p>
  <p class="count"><strong>60</strong> Capsules <span class="divider"></span> <strong>375</strong>mg</p>

  <section class="facts">
    <h2>Supplement Facts</h2>
    <p>Serving Size: 2 Capsules</p>
    <p>Servings Per Container: 30</p>
    <div class="rule-thick"></div>
    <div class="row head"><span>Amount per serving</span><span>%DV</span></div>
    <div class="row"><span>Calories</span><span></span></div>
    <div class="rule"></div>
    <div class="row nutrient"><span>Nicotinamide Riboside</span><span>1000mg</span><span>5000%</span></div>
    <div class="rule"></div>
    <div class="row"><span>*Percent daily values (DV)</span><span>5000%</span></div>
  </section>

  <p class="ingredients"><b>Other Ingredients:</b> Vegetable cellulose (capsule)</p>
  <div class="distributor">
    <b>Distributed By:</b>
    <span>Silverpine Biologics LLC,<br>Las Vegas NV<br>(555) 555-0187<br>www.SilverpineBiologics.example<br>Info@SilverpineBiologics.example</span>
  </div>
</div>
</body>
</html>
```